TVF web design

We need a homepage web design concept for a new company based in Brisbane called 'Tarvel Fabrication'. They design, manufacture and repair of all forms of operator Roll Over Protective Structures or ROPS, and Falling Object Protective Structures or FOPS canopies and cabins.
Updates
Sorry link to website is incorrect should be http://www.norbeckfab.com.au/
Thanks
Hi Everyone
I am presenting designs to my client on Wednesday so will let you feedback.
Cheers
Mags
Target Market(s)
Adults in construction industry and their Agents/Distributors
Industry/Entity Type
Construction
Number of Pages Required
1 page
Requirements
Must have
- Main Navigation
- o Home
- o About Us
- - Mission and Values
- - Facilities
- - Terms and Conditions
- - Jobs
- o Rops/Fops
- o Cabins
- o Crane Repairs
- o Other Products
- o Links
- o Contact Us
- - Client wants a sleek, corporate look and feel an example of a site they like is www.corvinlode.com.au
- - Client is rebranding and I have attached some sample new brochures that contains their new corporate colours etc as a guideline for the direction they are going.
- - The following elements are to be included in the design concept:
- o Homepage
- - Room for a Flash banner of rotating images in banner
- - Phone number should appear on every page 07 4819 6307
- - Horizontal navigation (can you show how drop down will appear as well)
- - Logo is attached (bear in mind this will be changing to new corporate colours) so just use the one attached but colours need to be in line with their new colours.
- - Tagline is “It’s the choice you make, not the change you take that determines your safety!” this needs to be displayed on every page of the site.
- - New Corporate colours are orange: RGB - 239 - 179 - 47 (colour 1) to RGB 239 - 121 - 47 (colour 2) and grey: RGB - 46 - 54 – 64
- - Intro text on page somewhere
- - 3 containers/icons to highlight areas on site – Rops/Fops, Sign up to our enewsletter and Contact Us
- - Images – have attached a few that can be used in concepts.

```html
<!DOCTYPE html>
<html lang="en">
<head>
<meta charset="utf-8">
<title>Tarvel Fabrication – Homepage Concept</title>
<link href="https://fonts.googleapis.com/css2?family=Source+Sans+3:wght@400;600;700&display=swap" rel="stylesheet">
<style>
:root{
  --orange:#ef792f;
  --orange-light:#efb32f;
  --orange-band:#f25f16;
  --grey:#2e3640;
  --ink:#333a40;
  --paper:#dfe6e6;
  --nav:#15181c;
  --side:#0d0e10;
  --white:#ffffff;
}
*{box-sizing:border-box;margin:0;padding:0}
html,body{width:1200px;height:2560px;overflow:hidden;background:var(--white)}
body{font-family:"Source Sans 3",Arial,sans-serif}
.board{position:relative;width:1120px;height:2389px;transform:scale(1.0714);transform-origin:0 0}
.stage{position:absolute;left:67px;width:994px;background:linear-gradient(#08090a 0%,#141920 45%,#263244 100%)}
.site{position:absolute;left:97px;top:59px;width:800px;overflow:hidden;border:1px solid #8a949c;background:var(--paper)}
.side-band{position:absolute;left:0;top:0;width:100px;height:100%}
.header{position:absolute;left:91px;top:0;width:709px;height:50px;background:var(--grey);border-bottom:1px solid #56606a}
.logo{position:absolute;left:26px;top:12px;height:25px;padding:0 10px;border:2px solid var(--orange);border-radius:5px;color:var(--orange);font-size:16px;font-weight:600;letter-spacing:.5px;line-height:21px;text-transform:uppercase}
.banner{position:absolute;left:91px;top:50px;width:709px;height:90px;background:linear-gradient(90deg,#3a3020 0%,#b8902a 22%,#2a2416 40%,#8a8c90 55%,#c9ccd2 68%,#5a5e66 80%,#2e3640 100%)}
.tagline{position:absolute;right:0;top:8px;width:244px;height:79px;background:rgba(46,54,64,.85);border-radius:10px 0 0 10px;color:var(--white);font-size:12.5px;line-height:17px;padding:14px 0 0 10px;text-transform:uppercase}
.tagline span{display:block}
.tagline .mid{padding-left:26px}
.nav{position:absolute;left:91px;top:140px;width:709px;height:35px;background:var(--nav);list-style:none}
.nav li{position:absolute;top:6px;height:24px;border:2px solid var(--orange);border-radius:6px;color:#e8ecee;font-size:11px;line-height:20px;text-align:center;text-transform:uppercase}
.nav li.active{border-color:var(--white);color:var(--orange)}
.dropdown{position:absolute;left:179px;top:175px;width:150px;background:var(--grey);list-style:none;padding-top:2px;z-index:2}
.dropdown li{height:20px;padding-left:6px;color:#e8ecee;font-size:9.5px;line-height:20px;text-transform:uppercase}
.dropdown li.hover{background:var(--orange);color:var(--white)}
.content{position:absolute;left:117px;top:202px;width:470px;color:var(--ink)}
.content h1{font-size:29px;font-weight:400;color:var(--orange);text-transform:uppercase;margin-bottom:14px}
.content p{font-size:10.6px;line-height:14.5px;margin-bottom:14.5px}
.sidebar{position:absolute;left:640px;top:175px;width:160px;bottom:0;background:var(--side)}
.phone{position:absolute;left:0;top:13px;width:160px;height:32px;background:linear-gradient(90deg,var(--orange-light),var(--orange) 40%)}
.phone .icon{position:absolute;left:14px;top:-1px;width:38px;height:34px;border:2px solid var(--white);border-radius:6px;background:var(--orange)}
.phone .num{position:absolute;left:64px;top:0;color:var(--white);font-weight:700;font-size:14px;line-height:32px}
.tile-img{position:absolute;left:0;width:160px}
.tile-label{position:absolute;left:0;width:160px;height:24px;background:linear-gradient(90deg,var(--orange),var(--orange-light));color:var(--white);font-weight:600;font-size:15px;line-height:24px;padding-left:13px;text-transform:uppercase}
.tile-label svg{position:absolute;right:8px;top:5px}
.news{position:absolute;left:0;top:173px;width:160px;height:37px;background:linear-gradient(90deg,var(--orange),var(--orange-light) 140%)}
.news .badge{position:absolute;left:10px;top:-2px;width:40px;height:40px;border:2px solid var(--white);border-radius:50%;color:var(--white);font-size:24px;font-weight:700;text-align:center;line-height:35px}
.news .copy{position:absolute;left:64px;top:3px;color:var(--white);font-size:12px;font-weight:600;line-height:14px}
</style>
</head>
<body>
<div class="board">

<!-- Screen 1: Home -->
<section class="stage" style="top:96px;height:619px">
  <div class="site" style="height:501px">
    <svg class="side-band" viewBox="0 0 100 501" preserveAspectRatio="none" role="img" aria-label="Orange side band with soft light sweep">
      <defs><linearGradient id="sweep1" x1="0" y1="0" x2="1" y2="0"><stop offset="0" stop-color="#ffffff" stop-opacity=".9"/><stop offset="1" stop-color="#ffffff" stop-opacity="0"/></linearGradient></defs>
      <path d="M86 0H96C92 210 76 390 48 501H30C60 385 80 205 86 0Z" fill="url(#sweep1)"/>
      <path d="M0 0H86C80 205 60 385 30 501H0Z" fill="var(--orange-band)"/>
    </svg>
    <header class="header"><div class="logo">Tarvel Fabrication</div></header>
    <div class="banner" role="img" aria-label="Rotating banner of workshop photos: cabins, ROPS frames and crane booms">
      <div class="tagline"><span>“It’s the choice you make,</span><span class="mid">not the change you take that</span><span>determines your safety!”</span></div>
    </div>
    <ul class="nav">
      <li style="left:26px;width:49px">Home</li><li style="left:88px;width:68px">About Us</li><li style="left:170px;width:72px">Rops/Fops</li><li style="left:255px;width:55px">Cabins</li><li style="left:323px;width:92px">Crane Repairs</li><li style="left:429px;width:107px">Other Products</li><li style="left:549px;width:44px">Links</li><li style="left:606px;width:80px">Contact Us</li>
    </ul>
    <article class="content">
      <h1>Welcome</h1>
      <p>Lorem ipsum dolor sit amet, consectetur adipiscing elit. Sed tincidunt accumsan scelerisque. Sed vestibulum fringilla velit, in interdum tortor suscipit sed. Maecenas tellus arcu, faucibus id pulvinar et, tempus ut nunc. Maecenas enim velit, hendrerit sit amet placerat et, tristique vel risus. Nullam ultrices mi erat.</p>
      <p>Praesent nisl felis, ornare in posuere vitae, hendrerit tempor risus. Curabitur commodo dui in est ornare id dictum ipsum tempor. Pellentesque habitant morbi tristique senectus et netus et malesuada fames ac turpis egestas. Etiam at ultrices libero. Nunc vehicula suscipit justo eget tempor. Sed quis nisl nisl. Quisque justo ipsum, ornare eu euismod a, laoreet quis metus. Ut mollis, mauris ac dignissim convallis, eros turpis hendrerit leo, quis viverra mauris lacus at mauris. Proin augue nibh, vestibulum eget malesuada sed, vehicula in lectus. Vestibulum imperdiet rhoncus leo, vitae mollis orci congue quis. Donec quis ligula sem, eget porta nulla. Suspendisse potenti. Donec porta elementum ipsum, sed commodo mi consequat quis. Quisque vehicula eleifend dignissim.</p>
    </article>
    <aside class="sidebar">
      <div class="phone"><div class="icon"><svg width="34" height="30" viewBox="0 0 34 30"><path d="M8 12c0-4 4-6 9-6s9 2 9 6h-4v-2h-10v2zM10 13h14l3 9H7z" fill="#fff"/><circle cx="17" cy="18" r="2.5" fill="#ef792f"/></svg></div><span class="num">07 4819 6307</span></div>
      <div class="tile-img" style="top:65px;height:65px;background:linear-gradient(90deg,#d06418,#ef9a2f 60%,#c88a20)" role="img" aria-label="Orange-toned photo of a ROPS cabin frame"></div>
      <div class="tile-label" style="top:130px">Rops/Fops<svg width="18" height="14" viewBox="0 0 18 14"><path d="M2 1l6 6-6 6M9 1l6 6-6 6" fill="none" stroke="#fff" stroke-width="2"/></svg></div>
      <div class="news"><div class="badge">@</div><div class="copy">Sign up to<br>our enewsletter</div></div>
      <div class="tile-img" style="top:235px;height:67px;background:linear-gradient(90deg,#bfe6f2,#e9f4f8 55%,#a8b4bc)" role="img" aria-label="Photo of a customer service operator with headset"></div>
      <div class="tile-label" style="top:302px">Contact Us<svg width="18" height="14" viewBox="0 0 18 14"><path d="M2 1l6 6-6 6M9 1l6 6-6 6" fill="none" stroke="#fff" stroke-width="2"/></svg></div>
    </aside>
  </div>
</section>

<!-- Screen 2: About Us drop-down -->
<section class="stage" style="top:796px;height:619px">
  <div class="site" style="height:501px">
    <svg class="side-band" viewBox="0 0 100 501" preserveAspectRatio="none" role="img" aria-label="Orange side band with soft light sweep">
      <defs><linearGradient id="sweep2" x1="0" y1="0" x2="1" y2="0"><stop offset="0" stop-color="#ffffff" stop-opacity=".9"/><stop offset="1" stop-color="#ffffff" stop-opacity="0"/></linearGradient></defs>
      <path d="M86 0H96C92 210 76 390 48 501H30C60 385 80 205 86 0Z" fill="url(#sweep2)"/>
      <path d="M0 0H86C80 205 60 385 30 501H0Z" fill="var(--orange-band)"/>
    </svg>
    <header class="header"><div class="logo">Tarvel Fabrication</div></header>
    <div class="banner" role="img" aria-label="Rotating banner of workshop photos: cabins, ROPS frames and crane booms">
      <div class="tagline"><span>“It’s the choice you make,</span><span class="mid">not the change you take that</span><span>determines your safety!”</span></div>
    </div>
    <ul class="nav">
      <li style="left:26px;width:49px">Home</li><li class="active" style="left:88px;width:68px">About Us</li><li style="left:170px;width:72px">Rops/Fops</li><li style="left:255px;width:55px">Cabins</li><li style="left:323px;width:92px">Crane Repairs</li><li style="left:429px;width:107px">Other Products</li><li style="left:549px;width:44px">Links</li><li style="left:606px;width:80px">Contact Us</li>
    </ul>
    <ul class="dropdown">
      <li>[ Mission and Values ]</li><li>[ Facilities ]</li><li class="hover">[ Terms and Conditions ]</li><li>[ Jobs ]</li>
    </ul>
    <article class="content">
      <h1>Welcome</h1>
      <p>Lorem ipsum dolor sit amet, consectetur adipiscing elit. Sed tincidunt accumsan scelerisque. Sed vestibulum fringilla velit, in interdum tortor suscipit sed. Maecenas tellus arcu, faucibus id pulvinar et, tempus ut nunc. Maecenas enim velit, hendrerit sit amet placerat et, tristique vel risus. Nullam ultrices mi erat.</p>
      <p>Praesent nisl felis, ornare in posuere vitae, hendrerit tempor risus. Curabitur commodo dui in est ornare id dictum ipsum tempor. Pellentesque habitant morbi tristique senectus et netus et malesuada fames ac turpis egestas. Etiam at ultrices libero. Nunc vehicula suscipit justo eget tempor. Sed quis nisl nisl. Quisque justo ipsum, ornare eu euismod a, laoreet quis metus. Ut mollis, mauris ac dignissim convallis, eros turpis hendrerit leo, quis viverra mauris lacus at mauris. Proin augue nibh, vestibulum eget malesuada sed, vehicula in lectus. Vestibulum imperdiet rhoncus leo, vitae mollis orci congue quis. Donec quis ligula sem, eget porta nulla. Suspendisse potenti. Donec porta elementum ipsum, sed commodo mi consequat quis. Quisque vehicula eleifend dignissim.</p>
    </article>
    <aside class="sidebar">
      <div class="phone"><div class="icon"><svg width="34" height="30" viewBox="0 0 34 30"><path d="M8 12c0-4 4-6 9-6s9 2 9 6h-4v-2h-10v2zM10 13h14l3 9H7z" fill="#fff"/><circle cx="17" cy="18" r="2.5" fill="#ef792f"/></svg></div><span class="num">07 4819 6307</span></div>
      <div class="tile-img" style="top:65px;height:65px;background:linear-gradient(90deg,#d06418,#ef9a2f 60%,#c88a20)" role="img" aria-label="Orange-toned photo of a ROPS cabin frame"></div>
      <div class="tile-label" style="top:130px">Rops/Fops<svg width="18" height="14" viewBox="0 0 18 14"><path d="M2 1l6 6-6 6M9 1l6 6-6 6" fill="none" stroke="#fff" stroke-width="2"/></svg></div>
      <div class="news"><div class="badge">@</div><div class="copy">Sign up to<br>our enewsletter</div></div>
      <div class="tile-img" style="top:235px;height:67px;background:linear-gradient(90deg,#bfe6f2,#e9f4f8 55%,#a8b4bc)" role="img" aria-label="Photo of a customer service operator with headset"></div>
      <div class="tile-label" style="top:302px">Contact Us<svg width="18" height="14" viewBox="0 0 18 14"><path d="M2 1l6 6-6 6M9 1l6 6-6 6" fill="none" stroke="#fff" stroke-width="2"/></svg></div>
    </aside>
  </div>
</section>

<!-- Screen 3: About Us page -->
<section class="stage" style="top:1496px;height:800px">
  <div class="site" style="height:650px">
    <svg class="side-band" viewBox="0 0 100 650" preserveAspectRatio="none" role="img" aria-label="Orange side band with soft light sweep">
      <defs><linearGradient id="sweep3" x1="0" y1="0" x2="1" y2="0"><stop offset="0" stop-color="#ffffff" stop-opacity=".9"/><stop offset="1" stop-color="#ffffff" stop-opacity="0"/></linearGradient></defs>
      <path d="M86 0H96C92 270 76 505 48 650H30C60 500 80 265 86 0Z" fill="url(#sweep3)"/>
      <path d="M0 0H86C80 265 60 500 30 650H0Z" fill="var(--orange-band)"/>
    </svg>
    <header class="header"><div class="logo">Tarvel Fabrication</div></header>
    <div class="banner" role="img" aria-label="Rotating banner of workshop photos: cabins, ROPS frames and crane booms">
      <div class="tagline"><span>“It’s the choice you make,</span><span class="mid">not the change you take that</span><span>determines your safety!”</span></div>
    </div>
    <ul class="nav">
      <li style="left:26px;width:49px">Home</li><li class="active" style="left:88px;width:68px">About Us</li><li style="left:170px;width:72px">Rops/Fops</li><li style="left:255px;width:55px">Cabins</li><li style="left:323px;width:92px">Crane Repairs</li><li style="left:429px;width:107px">Other Products</li><li style="left:549px;width:44px">Links</li><li style="left:606px;width:80px">Contact Us</li>
    </ul>
    <article class="content">
      <h1>About Us</h1>
      <p>Lorem ipsum dolor sit amet, consectetur adipiscing elit. Sed tincidunt accumsan scelerisque. Sed vestibulum fringilla velit, in interdum tortor suscipit sed. Maecenas tellus arcu, faucibus id pulvinar et, tempus ut nunc. Maecenas enim velit, hendrerit sit amet placerat et, tristique vel risus. Nullam ultrices mi erat.</p>
      <p>Praesent nisl felis, ornare in posuere vitae, hendrerit tempor risus. Curabitur commodo dui in est ornare id dictum ipsum tempor. Pellentesque habitant morbi tristique senectus et netus et malesuada fames ac turpis egestas. Etiam at ultrices libero. Nunc vehicula suscipit justo eget tempor. Sed quis nisl nisl. Quisque justo ipsum, ornare eu euismod a, laoreet quis metus. Ut mollis, mauris ac dignissim convallis, eros turpis hendrerit leo, quis viverra mauris lacus at mauris. Proin augue nibh, vestibulum eget malesuada sed, vehicula in lectus. Vestibulum imperdiet rhoncus leo, vitae mollis orci congue quis. Donec quis ligula sem, eget porta nulla. Suspendisse potenti. Donec porta elementum ipsum, sed commodo mi consequat quis. Quisque vehicula eleifend dignissim.</p>
      <p>Cras commodo varius mi vel ultricies. Curabitur dictum placerat neque, ac blandit odio viverra vitae. Maecenas id lorem sit amet eros egestas accumsan. Cras non vulputate tortor. Nam aliquam accumsan aliquet. Suspendisse ac orci nisl, vel vestibulum ligula. Integer vel tortor ante. Curabitur tincidunt tortor id est dignissim egestas. Nullam non erat ante. Class aptent taciti sociosqu ad litora torquent per conubia nostra, per inceptos himenaeos. Donec vitae dui vel lectus sodales volutpat non quis lorem. Nunc felis metus, posuere at pretium sed, molestie varius orci. Donec vitae ligula est. Maecenas eget leo sapien. Mauris pharetra viverra tortor et tempus. Vivamus purus lacus, tempor in venenatis sollicitudin, elementum ut dui. Morbi feugiat tristique nisl, eu elementum tortor aliquet non. Nunc suscipit mi vel ipsum pellentesque mattis. Cras vehicula eleifend nunc non bibendum.</p>
    </article>
    <aside class="sidebar">
      <div class="phone"><div class="icon"><svg width="34" height="30" viewBox="0 0 34 30"><path d="M8 12c0-4 4-6 9-6s9 2 9 6h-4v-2h-10v2zM10 13h14l3 9H7z" fill="#fff"/><circle cx="17" cy="18" r="2.5" fill="#ef792f"/></svg></div><span class="num">07 4819 6307</span></div>
      <div class="tile-img" style="top:65px;height:65px;background:linear-gradient(90deg,#d06418,#ef9a2f 60%,#c88a20)" role="img" aria-label="Orange-toned photo of a ROPS cabin frame"></div>
      <div class="tile-label" style="top:130px">Rops/Fops<svg width="18" height="14" viewBox="0 0 18 14"><path d="M2 1l6 6-6 6M9 1l6 6-6 6" fill="none" stroke="#fff" stroke-width="2"/></svg></div>
      <div class="news"><div class="badge">@</div><div class="copy">Sign up to<br>our enewsletter</div></div>
      <div class="tile-img" style="top:235px;height:67px;background:linear-gradient(90deg,#bfe6f2,#e9f4f8 55%,#a8b4bc)" role="img" aria-label="Photo of a customer service operator with headset"></div>
      <div class="tile-label" style="top:302px">Contact Us<svg width="18" height="14" viewBox="0 0 18 14"><path d="M2 1l6 6-6 6M9 1l6 6-6 6" fill="none" stroke="#fff" stroke-width="2"/></svg></div>
    </aside>
  </div>
</section>

</div>
</body>
</html>
```